Tradeline Summit & Fair xmas banner/MREC promotion

Size:
• Leader board: 728 x 90 px
• MREC: 300 x250 px
• Half-page: 300 x 600
• Wide skyscraper: 160 x 600
Image:
Candy cane stripes as the background – image bought. Horizontal or vertical whatever you think will works.
White strip/background for the copy? See images example – unless you don’t need to do that?
Bold font which is "neutra" to our other banners attached. I think black font would look good.
Message:
Please give it a good readable pace between slides – 3 secs?
1st Slide
It’s silly season!
2nd Slide
Treat yourself to an end of year gift
3rd Slide
Book your ticket now and save $$$
4th Slide
Get spoilt. You’re worth it!
5th Slide
Tradeline logo
Target Market(s)
anyone that sells online
• Automotive • Advertising • Digital • Entertainment
• Finance • Hospitality • Pharmaceutical/Healthcare • Pop Culture
• Retail • Travel • Telecommunications

```html
<!DOCTYPE html>
<html lang="en">
<head>
<meta charset="utf-8">
<title>Tradeline Summit &amp; Fair – Half-page 300 x 600 sequence</title>
<link rel="stylesheet" href="https://fonts.googleapis.com/css2?family=League+Spartan:wght@400;700&display=swap">
<style>
  :root {
    --board: #1a1a1a;
    --label: #ffffff;
    --ink: #000000;
    --glow: #ffffff;
    --cane-white: #fbf3ee;
    --cane-pink: #efc2b8;
    --cane-red: #c8261e;
    --cane-deep: #6a0f0c;
    --shadow: #3a3a3a;
  }
  * { margin: 0; padding: 0; box-sizing: border-box; }
  html, body {
    width: 1200px;
    height: 1000px;
    overflow: hidden;
    background: var(--board);
  }
  .presentation-board {
    position: relative;
    width: 1200px;
    height: 1000px;
    background: var(--board);
    font-family: "League Spartan", "Helvetica Neue", Arial, sans-serif;
  }
  .size-label {
    position: absolute;
    left: 76px;
    top: 30px;
    color: var(--label);
    font-weight: 700;
    font-size: 11px;
    letter-spacing: 0.04em;
    text-transform: uppercase;
  }
  .frame-strip {
    position: absolute;
    left: 87px;
    top: 279px;
    display: flex;
    gap: 13.5px;
  }
  .banner-frame {
    position: relative;
    width: 192px;
    height: 381px;
    box-shadow: 0 3px 0 var(--shadow);
  }
  .candy-backdrop {
    position: absolute;
    inset: 0;
    background:
      radial-gradient(ellipse 62% 48% at 50% 50%,
        var(--cane-white) 0%,
        var(--cane-white) 35%,
        var(--cane-pink) 62%,
        var(--cane-red) 86%,
        var(--cane-deep) 100%);
  }
  .slide-copy {
    position: absolute;
    inset: 0;
    display: flex;
    align-items: center;
    justify-content: center;
    text-align: center;
    padding: 0 18px;
    color: var(--ink);
    font-weight: 700;
    font-size: 19px;
    line-height: 23px;
    text-transform: uppercase;
    text-shadow:
      0 0 3px var(--glow),
      0 0 6px var(--glow),
      0 0 10px var(--glow);
  }
  .brand-lockup {
    position: absolute;
    inset: 0;
    display: flex;
    flex-direction: column;
    align-items: center;
    justify-content: center;
    color: var(--ink);
    font-weight: 400;
  }
  .brand-name {
    font-size: 27px;
    line-height: 26px;
    letter-spacing: 0.01em;
  }
  .brand-descriptor {
    align-self: flex-end;
    margin-right: 28px;
    font-size: 9px;
    line-height: 10px;
  }
</style>
</head>
<body>
  <main class="presentation-board">
    <p class="size-label">Half-page: 300 x 600</p>

    <section class="frame-strip" aria-label="Half-page banner slides">
      <article class="banner-frame">
        <div class="candy-backdrop" role="img" aria-label="Candy cane stripes photo with a soft white glow in the centre"></div>
        <p class="slide-copy">It’s silly<br>season!</p>
      </article>

      <article class="banner-frame">
        <div class="candy-backdrop" role="img" aria-label="Candy cane stripes photo with a soft white glow in the centre"></div>
        <p class="slide-copy">Treat<br>yourself to<br>an end of<br>year gift</p>
      </article>

      <article class="banner-frame">
        <div class="candy-backdrop" role="img" aria-label="Candy cane stripes photo with a soft white glow in the centre"></div>
        <p class="slide-copy">Book your<br>ticket now<br>and save $$$</p>
      </article>

      <article class="banner-frame">
        <div class="candy-backdrop" role="img" aria-label="Candy cane stripes photo with a soft white glow in the centre"></div>
        <p class="slide-copy">Get spoilt.<br>You’re<br>worth it!</p>
      </article>

      <article class="banner-frame">
        <div class="candy-backdrop" role="img" aria-label="Candy cane stripes photo with a soft white glow in the centre"></div>
        <div class="brand-lockup">
          <span class="brand-name">Tradeline</span>
          <span class="brand-descriptor">Summit &amp; Fair</span>
        </div>
      </article>
    </section>
  </main>
</body>
</html>
```